Professional Website for Corvell Laundry Company

Corvell Laundry Company is a family-owned laundry service provider that has been serving Midtown Atlanta for over 45 years. We provide express clothing and linen washing services to residential and commercial clients in Atlanta and surrounding areas.

The final website and logo design should convey professionalism and give the customer a sense of security in having their personal items laundered with us.

Target Market(s)

Commercial Businesses and high net worth personal customers

Industry/Entity Type

Professional Laundry Services

Coding

Coded - Design and coding required

Number of Pages Required

5+ page

Font styles to use
Sans Serif

Colors
0054AA
0677BA
7BADD7
CADEEF
E8F1F8

Requirements
Must have
• I would like to have the following elements on my website: 1. Blog page 2. Contact Us Form 3. Sign up for service (sample attached) 4. Sections outlined in the content copy page 5. Links to social media accounts.
Nice to have
• A great example is https://www.quorvadip.example/laundry-pick-up-and-delivery/?utm_term=pick%20up%20and%20delivery%20laundry%20service&utm_campaign=*QV%20United%20States%20%7C%20Search%20(Broad%20KWs)&utm_source=bing&utm_medium=ppc&hsa_acc=1203948576&hsa_cam=50219384761&hsa_grp=9081726354637281&hsa_ad=&hsa_src=o&hsa_tgt=kwd-27391046582917:loc-190&hsa_kw=pick%20up%20and%20delivery%20laundry%20service&hsa_mt=e&hsa_net=bing&hsa_ver=3&msclkid=3a9f0c1b2d4e5f60718293a4b5c6d7e8

```html
<!DOCTYPE html>
<html lang="en">
<head>
<meta charset="utf-8">
<title>Corvell Laundry Company</title>
<link href="https://fonts.googleapis.com/css2?family=Poppins:wght@400;500;600;700;800&display=swap" rel="stylesheet">
<style>
:root{
  --blue-deep:#0054AA;
  --blue:#0677BA;
  --blue-bright:#1574d4;
  --blue-soft:#7BADD7;
  --blue-pale:#CADEEF;
  --blue-mist:#E8F1F8;
  --navy:#0a3f86;
  --ink:#1d2a3a;
  --muted:#6b7686;
  --line:#d9e2ec;
  --white:#ffffff;
}
*{box-sizing:border-box;margin:0;padding:0}
html,body{width:1200px;height:3116px;overflow:hidden}
body{font-family:'Poppins',sans-serif;color:var(--ink);background:var(--white);font-size:12px;line-height:1.6}
.wrap{width:840px;margin:0 auto;position:relative}
.btn{display:inline-block;background:var(--blue-bright);color:var(--white);font-weight:600;font-size:11px;padding:9px 20px;border-radius:3px;white-space:nowrap}
.btn.light{background:var(--white);color:var(--blue-deep)}
.logo{display:flex;align-items:center;gap:8px;font-weight:700;font-size:13px;color:var(--white);white-space:nowrap}
.logo .dot{width:26px;height:26px;border-radius:50%;background:var(--white);flex:none}

/* hero */
.hero{position:relative;height:460px;background:linear-gradient(180deg,#f4f7fa,#e9eef3)}
.hero-photo{position:absolute;right:0;top:0;width:620px;height:460px;background:linear-gradient(135deg,#c7d2dc,#8e9eab 55%,#dfe6ec)}
.topbar{position:absolute;left:0;top:0;width:600px;height:22px;background:var(--blue-deep);color:var(--white);font-size:9px;display:flex;align-items:center;gap:26px;padding-left:180px}
.nav{position:absolute;left:180px;right:180px;top:32px;height:44px;display:flex;align-items:center;justify-content:space-between}
.nav .logo{color:var(--blue-deep)}
.nav .logo .dot{background:var(--blue-deep)}
.nav ul{display:flex;gap:34px;list-style:none;font-size:11px;font-weight:500;color:var(--ink)}
.nav ul li:first-child{color:var(--blue-bright)}
.hero-copy{position:absolute;left:180px;top:148px;width:360px}
.eyebrow{color:var(--blue-bright);font-weight:600;font-size:12px;margin-bottom:6px}
.hero h1{font-size:44px;line-height:1.15;font-weight:800;color:var(--blue-deep);margin-bottom:26px}

/* about */
.about{height:230px;background:var(--blue-bright);color:var(--white);padding-top:42px}
.about h2{font-size:18px;font-weight:700;margin-bottom:14px}
.about p{font-size:10px;line-height:1.75;opacity:.92;margin-bottom:10px}

/* services */
.services{height:400px;position:relative}
.svc-photo{position:absolute;left:180px;top:50px;width:340px;height:310px;background:linear-gradient(160deg,#e3d9cf,#b9a998 60%,#d8cfc4)}
.badge{position:absolute;left:148px;top:160px;width:136px;height:66px;background:var(--blue-bright);color:var(--white);border-radius:4px;display:flex;align-items:center;gap:10px;padding:0 12px;white-space:nowrap}
.badge .ring{width:28px;height:28px;border-radius:50%;border:2px solid var(--white);flex:none}
.badge b{font-size:17px;display:block;line-height:1.15}
.badge span.lbl{font-size:8px;display:block;line-height:1.3}
.svc-panel{position:absolute;left:520px;top:70px;width:500px;height:280px;background:#f1f3f6;padding:24px 34px}
.svc-panel h2{color:var(--blue-bright);font-size:20px;font-weight:700;margin-bottom:6px}
.svc-panel p{font-size:9px;color:var(--muted);line-height:1.7;margin-bottom:14px}
.svc-list{display:grid;grid-template-columns:1fr 1fr;gap:7px 20px;list-style:none;font-size:9.5px;margin-bottom:22px}
.svc-list li{display:flex;align-items:center;gap:7px}
.tick{width:11px;height:11px;flex:none}
.svc-foot{display:flex;align-items:center;gap:26px}
.call{display:flex;align-items:center;gap:8px;font-size:8px;color:var(--muted)}
.call b{display:block;font-size:13px;color:var(--blue-deep)}
.call .ic{width:26px;height:26px;border-radius:50%;background:var(--blue-bright);display:flex;align-items:center;justify-content:center}

/* why */
.why{height:700px;background:linear-gradient(180deg,#f5f8fb,#eef3f8);border-top:1px solid var(--line);padding-top:36px}
.why h2{font-size:22px;font-weight:700;color:var(--blue-deep);margin-bottom:18px}
.why-grid{display:flex;gap:40px}
.form-card{width:320px;height:590px;background:var(--white);padding:22px 22px;box-shadow:0 2px 10px rgba(0,60,120,.06)}
.form-card h3{font-size:11px;color:var(--blue-deep);font-weight:600;margin-bottom:4px}
.form-card .lead{font-size:8.5px;color:var(--muted);line-height:1.6;margin-bottom:14px}
.field{font-size:8.5px;color:var(--muted);margin-bottom:4px}
.input{height:26px;border:1px solid var(--line);border-radius:2px;margin-bottom:12px}
.radios{display:flex;gap:20px;font-size:8.5px;margin-bottom:14px}
.radios span{display:flex;align-items:center;gap:5px}
.radios i{width:10px;height:10px;border:1px solid var(--blue-soft);border-radius:50%}
.radios i.on{background:var(--blue-bright);border-color:var(--blue-bright)}
.textarea{height:92px;border:1px solid var(--line);border-radius:2px;margin-bottom:14px}
.features{flex:1;display:grid;grid-template-columns:1fr 1fr;gap:36px 30px;align-content:start;padding-top:10px}
.feature{display:flex;gap:10px}
.feature .fi{width:26px;height:26px;border-radius:50%;background:var(--blue-bright);flex:none;display:flex;align-items:center;justify-content:center}
.feature h4{font-size:10px;font-weight:600;line-height:1.35;margin-bottom:5px}
.feature p{font-size:8.5px;color:var(--muted);line-height:1.7}

/* setup */
.setup{height:320px;padding-top:36px}
.setup h2{font-size:16px;font-weight:700;color:var(--blue-deep);margin-bottom:14px}
.steps{display:flex}
.step{flex:1;height:226px;color:var(--white);padding:26px 26px}
.step:nth-child(1){background:var(--blue-deep)}
.step:nth-child(2){background:var(--blue-bright)}
.step:nth-child(3){background:var(--blue-soft)}
.step h3{font-size:17px;font-weight:600;margin-bottom:8px;line-height:1.3}
.step p{font-size:8.5px;line-height:1.7;opacity:.92;margin-bottom:14px}

/* faq */
.faq{height:450px;padding-top:22px}
.faq h2{font-size:14px;font-weight:700;margin-bottom:10px}
.faq-item{border-bottom:1px solid var(--line);padding:11px 0;display:flex;justify-content:space-between;font-size:10px;font-weight:500}
.faq-item .plus{color:var(--blue-bright);font-weight:600}
.faq-open{border-bottom:1px solid var(--line);padding:11px 0 14px}
.faq-open .q{display:flex;justify-content:space-between;font-size:10px;font-weight:600;color:var(--blue-deep);margin-bottom:6px}
.faq-open p{font-size:8.5px;color:var(--muted);margin-bottom:6px}
.faq-open ul{list-style:none;font-size:8.5px;color:var(--muted)}
.faq-open li{padding-left:12px;position:relative;line-height:1.9}
.faq-open li::before{content:"";position:absolute;left:0;top:7px;width:5px;height:5px;border-radius:50%;background:var(--blue-bright)}

/* cta */
.cta{height:300px;position:relative}
.cta-band{position:absolute;left:0;right:0;top:40px;height:240px;background:var(--blue-bright)}
.van{position:absolute;left:0;top:10px;width:440px;height:250px;background:linear-gradient(135deg,#eef4fb,#a9c9ea 70%,#1f4d8a);border-radius:0 8px 8px 0}
.cta-copy{position:absolute;left:600px;width:420px;top:118px;color:var(--white);display:flex;justify-content:space-between;align-items:flex-start;gap:20px}
.cta-copy h2{font-size:22px;font-weight:600;line-height:1.3;white-space:nowrap}
.cta-copy .btn{padding:6px 16px;font-size:9px;margin-top:4px}

/* footer */
.footer{height:256px;background:var(--blue-deep);color:var(--white)}
.foot-main{display:flex;gap:60px;padding-top:40px;height:200px}
.foot-brand{width:220px}
.foot-brand p{font-size:13px;font-weight:600;line-height:1.35;margin-top:16px}
.foot-col h5{font-size:10px;font-weight:600;margin-bottom:10px}
.foot-col a{display:block;font-size:8.5px;opacity:.85;line-height:2}
.foot-col.news{margin-left:auto;width:200px}
.foot-col.news p{font-size:8.5px;opacity:.85;margin-bottom:8px}
.sub{display:flex}
.sub .in{flex:1;height:24px;background:var(--white)}
.sub .go{width:40px;height:24px;background:var(--blue-soft)}
.foot-bar{height:56px;background:var(--navy);font-size:8.5px;display:flex;align-items:center}
.foot-bar .wrap{display:flex;justify-content:space-between;opacity:.85}
</style>
</head>
<body>

<section class="hero">
  <div class="hero-photo" role="img" aria-label="Photo of hands loading laundry into a front-loading washing machine"></div>
  <div class="topbar"><span>hello@corvell-laundry.example</span><span>412 Peachtree Lane, Atlanta GA</span></div>
  <nav class="nav">
    <div class="logo"><span class="dot"></span>Corvell Laundry Company</div>
    <ul><li>Home</li><li>Services</li><li>About</li><li>Blog</li><li>Contact</li></ul>
    <span class="btn">Schedule Pickup</span>
  </nav>
  <div class="hero-copy">
    <div class="eyebrow">We are Passionate About Laundry</div>
    <h1>Laundry &amp;<br>Dry Cleaning<br>Service</h1>
    <span class="btn">Schedule a Pickup</span>
  </div>
</section>

<section class="about">
  <div class="wrap">
    <h2>About Us</h2>
    <p>Corvell Laundry Company is a family-owned laundry service provider that has been serving Midtown Atlanta for over 45 years. We provide express clothing and linen washing services to residential and commercial clients in Atlanta and the surrounding areas, with care taken on every single item we handle.</p>
    <p>Whether you have a busy household, a growing business or simply want your weekends back, our team takes the time to understand your needs. We wash, dry and fold with attention to detail, using quality detergents and modern equipment to return your garments fresh, clean and neatly packed.</p>
    <p>Our goal has always been simple: give our customers the security of knowing their personal items are in trusted hands. From pickup to delivery, we stay on schedule, we communicate clearly and we treat your clothing as if it were our own.</p>
  </div>
</section>

<section class="services">
  <div class="svc-photo" role="img" aria-label="Photo of a stack of freshly folded towels"></div>
  <div class="badge"><span class="ring"></span><div><b>5,500 +</b><span class="lbl">Customers Served</span></div></div>
  <div class="svc-panel">
    <h2>Our Services</h2>
    <p>We provide dependable laundry care for homes and businesses across Atlanta. Every order is sorted, treated and finished by trained staff, so you can count on consistent results week after week.</p>
    <ul class="svc-list">
      <li><svg class="tick" viewBox="0 0 12 12"><circle cx="6" cy="6" r="6" fill="#1574d4"/><path d="M3.3 6.2l1.8 1.8 3.6-3.8" stroke="#fff" stroke-width="1.4" fill="none"/></svg>Professional Laundry</li>
      <li><svg class="tick" viewBox="0 0 12 12"><circle cx="6" cy="6" r="6" fill="#1574d4"/><path d="M3.3 6.2l1.8 1.8 3.6-3.8" stroke="#fff" stroke-width="1.4" fill="none"/></svg>Dry Cleaning</li>
      <li><svg class="tick" viewBox="0 0 12 12"><circle cx="6" cy="6" r="6" fill="#1574d4"/><path d="M3.3 6.2l1.8 1.8 3.6-3.8" stroke="#fff" stroke-width="1.4" fill="none"/></svg>Light Industrial Services</li>
      <li><svg class="tick" viewBox="0 0 12 12"><circle cx="6" cy="6" r="6" fill="#1574d4"/><path d="M3.3 6.2l1.8 1.8 3.6-3.8" stroke="#fff" stroke-width="1.4" fill="none"/></svg>Wash &amp; Fold</li>
      <li><svg class="tick" viewBox="0 0 12 12"><circle cx="6" cy="6" r="6" fill="#1574d4"/><path d="M3.3 6.2l1.8 1.8 3.6-3.8" stroke="#fff" stroke-width="1.4" fill="none"/></svg>Professional Linen Services</li>
      <li><svg class="tick" viewBox="0 0 12 12"><circle cx="6" cy="6" r="6" fill="#1574d4"/><path d="M3.3 6.2l1.8 1.8 3.6-3.8" stroke="#fff" stroke-width="1.4" fill="none"/></svg>Ironing Service</li>
      <li><svg class="tick" viewBox="0 0 12 12"><circle cx="6" cy="6" r="6" fill="#1574d4"/><path d="M3.3 6.2l1.8 1.8 3.6-3.8" stroke="#fff" stroke-width="1.4" fill="none"/></svg>Pickup &amp; Delivery</li>
      <li><svg class="tick" viewBox="0 0 12 12"><circle cx="6" cy="6" r="6" fill="#1574d4"/><path d="M3.3 6.2l1.8 1.8 3.6-3.8" stroke="#fff" stroke-width="1.4" fill="none"/></svg>Alterations</li>
    </ul>
    <div class="svc-foot">
      <span class="btn">Discover More</span>
      <div class="call"><span class="ic"><svg width="12" height="12" viewBox="0 0 24 24"><path d="M6.6 10.8a15 15 0 006.6 6.6l2.2-2.2a1 1 0 011-.25 11.4 11.4 0 003.6.57 1 1 0 011 1V20a1 1 0 01-1 1A17 17 0 013 4a1 1 0 011-1h3.5a1 1 0 011 1c0 1.25.2 2.45.57 3.57a1 1 0 01-.25 1z" fill="#fff"/></svg></span><div>Call Us Anytime<b>+1 404 555 0187</b></div></div>
    </div>
  </div>
</section>

<section class="why">
  <div class="wrap">
    <h2>Why Choose Corvell Laundry Company</h2>
    <div class="why-grid">
      <div class="form-card">
        <h3>We Help You Optimize Your Time</h3>
        <p class="lead">Tell us a little about your laundry needs and our team will reach out to set up a plan that fits your schedule and budget.</p>
        <div class="field">First name *</div><div class="input"></div>
        <div class="field">Last name *</div><div class="input"></div>
        <div class="field">Management Company or Private Home? *</div>
        <div class="radios"><span><i class="on"></i>Management Company</span><span><i></i>Private Home</span></div>
        <div class="field">Email *</div><div class="input"></div>
        <div class="field">Cell Phone *</div><div class="input"></div>
        <div class="field">Additional Information</div><div class="textarea"></div>
        <span class="btn">Submit</span>
      </div>
      <div class="features">
        <div class="feature"><span class="fi"><svg width="12" height="12" viewBox="0 0 12 12"><path d="M2.5 6.2l2.3 2.3 4.7-5" stroke="#fff" stroke-width="1.6" fill="none"/></svg></span><div><h4>We Have Knowledgeable, Friendly Team Members</h4><p>Our staff are trained in fabric care and customer service, and they are always ready to answer questions about your order.</p></div></div>
        <div class="feature"><span class="fi"><svg width="12" height="12" viewBox="0 0 12 12"><path d="M2.5 6.2l2.3 2.3 4.7-5" stroke="#fff" stroke-width="1.6" fill="none"/></svg></span><div><h4>We Provide Payment Options</h4><p>Pay the way that suits you best, with flexible billing for households and monthly invoicing for business clients.</p></div></div>
        <div class="feature"><span class="fi"><svg width="12" height="12" viewBox="0 0 12 12"><path d="M2.5 6.2l2.3 2.3 4.7-5" stroke="#fff" stroke-width="1.6" fill="none"/></svg></span><div><h4>Our Facility is Bright, Clean and Comfortable</h4><p>Visit our Midtown location and see a tidy, well lit space where every load is handled with care.</p></div></div>
        <div class="feature"><span class="fi"><svg width="12" height="12" viewBox="0 0 12 12"><path d="M2.5 6.2l2.3 2.3 4.7-5" stroke="#fff" stroke-width="1.6" fill="none"/></svg></span><div><h4>We Provide Customized Business Solutions</h4><p>Restaurants, salons, gyms and offices rely on tailored linen programs built around their volume and timing.</p></div></div>
        <div class="feature"><span class="fi"><svg width="12" height="12" viewBox="0 0 12 12"><path d="M2.5 6.2l2.3 2.3 4.7-5" stroke="#fff" stroke-width="1.6" fill="none"/></svg></span><div><h4>We Utilize Modern, Industrial Size Washer and Dryer Equipment</h4><p>High capacity machines let us turn orders around quickly while staying gentle on your fabrics.</p></div></div>
        <div class="feature"><span class="fi"><svg width="12" height="12" viewBox="0 0 12 12"><path d="M2.5 6.2l2.3 2.3 4.7-5" stroke="#fff" stroke-width="1.6" fill="none"/></svg></span><div><h4>Centralized Location</h4><p>Our central Atlanta base makes pickup and delivery fast for neighborhoods across the metro area.</p></div></div>
      </div>
    </div>
  </div>
</section>

<section class="setup">
  <div class="wrap">
    <h2>Setting up Services</h2>
    <div class="steps">
      <div class="step"><h3>Sign Up</h3><p>Create an account in just a few minutes. Choose the services you need and tell us how often you would like us to come by.</p><span class="btn light">Sign Up</span></div>
      <div class="step"><h3>Fill Out a Customer Profile</h3><p>Share your preferences for detergents, folding and special care so every order comes back exactly the way you like it.</p><span class="btn light">Start Here</span></div>
      <div class="step"><h3>Schedule a Pickup</h3><p>Pick a time that works for you. Our driver collects your laundry and returns it fresh, clean and ready to wear.</p><span class="btn light">Call to Book</span></div>
    </div>
  </div>
</section>

<section class="faq">
  <div class="wrap">
    <h2>What to Expect</h2>
    <div class="faq-open">
      <div class="q"><span>Can I Customize My Service?</span><span>&minus;</span></div>
      <p>Yes. When you sign up, you can tell us exactly how you want your laundry handled. You can choose from the following:</p>
      <ul>
        <li>Frequency of Service</li>
        <li>Choice of Soaps, Softeners, Bleach and Dryer Sheets</li>
        <li>Choice of Water Temperature</li>
        <li>Choice of Dryer Temperature</li>
        <li>Folded versus Hanged</li>
        <li>Special Instructions</li>
      </ul>
    </div>
    <div class="faq-item"><span>Are Laundry Bags Provided?</span><span class="plus">+</span></div>
    <div class="faq-item"><span>What is the Turnaround Time?</span><span class="plus">+</span></div>
    <div class="faq-item"><span>How Do We Pay?</span><span class="plus">+</span></div>
    <div class="faq-item"><span>Do you Have a referral program?</span><span class="plus">+</span></div>
  </div>
</section>

<section class="cta">
  <div class="cta-band"></div>
  <div class="van" role="img" aria-label="Illustration of a delivery van with a clothes hanger on its side"></div>
  <div class="cta-copy">
    <h2>Do You Have Dirty Clothes?<br>+1 404 555 0187</h2>
    <span class="btn light">Order Now</span>
  </div>
</section>

<footer class="footer">
  <div class="wrap foot-main">
    <div class="foot-brand">
      <div class="logo"><span class="dot"></span>Corvell Laundry Company</div>
      <p>Cleaning Clothes Since 1978,<br>Serving Midtown</p>
    </div>
    <div class="foot-col"><h5>Explore</h5><a>Home</a><a>About</a><a>Blog</a><a>Contact</a></div>
    <div class="foot-col"><h5>Contact</h5><a>hello@corvell-laundry.example</a><a>+1 404 555 0187</a></div>
    <div class="foot-col news"><h5>Newsletter</h5><p>Subscribe to our newsletter for news and updates.</p><div class="sub"><span class="in"></span><span class="go"></span></div></div>
  </div>
  <div class="foot-bar"><div class="wrap"><span>&copy; Copyright 2024 by Corvell Laundry Company</span><span>Terms &amp; Conditions | Privacy Policy</span></div></div>
</footer>

</body>
</html>
```